Healthcare marketing Website design

This is for a healthcare marketing agency
All details and brief included in the files

I need the design to be incredible!

5 pages to be designed
Home page
About
Portfolio Page
Services
Start your project page

If you need more stock images - download preview images from kelmora pix so I can purchase at a later date

```html
<!DOCTYPE html>
<html lang="en">
<head>
<meta charset="utf-8">
<title>Start Your Project – Northwave Consulting</title>
<link rel="stylesheet" href="https://fonts.googleapis.com/css2?family=Quicksand:wght@500;600;700&family=Poppins:wght@400;500&display=swap">
<style>
:root{
  --blue:#03aeef;
  --navy:#1b2a4e;
  --ink:#1d2b4f;
  --pale:#eaf6fc;
  --line:#d9dde4;
  --orange:#ffa23a;
  --mint:#52e3c2;
  --white:#ffffff;
  --muted:#8a93a3;
}
*{box-sizing:border-box;margin:0;padding:0}
html,body{width:1200px;height:2178px;overflow:hidden}
body{position:relative;background:var(--pale);font-family:"Quicksand",sans-serif;color:var(--ink)}
.abs{position:absolute}
.site-header{left:0;top:0;width:1200px;height:70px;background:var(--white);box-shadow:0 2px 8px rgba(0,0,0,.06);z-index:3}
.brand{left:161px;top:18px;display:flex;align-items:center;gap:10px;font-size:26px;font-weight:600;color:var(--blue)}
.brand-mark{width:26px;height:26px;background:var(--blue);border-radius:4px}
.main-nav{top:26px;font-family:"Poppins",sans-serif;font-size:13.5px;font-weight:500;color:var(--ink)}
.hero{left:0;top:70px;width:1200px;height:327px;background:linear-gradient(100deg,#f4f6f8 0%,#eceff2 45%,#dfe3e8 70%,#c9ced6 100%)}
.hero-title{left:163px;top:188px;font-size:34px;font-weight:600;letter-spacing:.5px}
.crumbs{left:163px;top:234px;font-size:15px;font-weight:600}
.crumbs span{font-weight:500}
.bg-shapes{left:0;top:0}
.section-title{left:0;width:1200px;top:502px;text-align:center;color:var(--white);font-size:39px;font-weight:600;letter-spacing:1px}
.section-sub{left:0;width:1200px;top:558px;text-align:center;color:var(--white);font-size:19px;font-weight:500}
.form-card{left:242px;top:613px;width:731px;height:974px;background:var(--white);border-radius:10px;box-shadow:0 10px 30px rgba(3,174,239,.12)}
.q-row{left:308px;width:577px;height:24px;font-size:16px;font-weight:500}
.q-row .choices{position:absolute;right:0;top:0;display:flex;gap:18px}
.choice{display:flex;align-items:center;gap:8px}
.radio{width:13px;height:13px;border:1.5px solid var(--ink);border-radius:50%;position:relative}
.radio.on{border-color:var(--blue)}
.radio.on::after{content:"";position:absolute;left:2px;top:2px;width:6px;height:6px;border-radius:50%;background:var(--blue)}
.dash{left:308px;width:577px;border-top:1px dashed var(--line)}
.field-label{left:308px;font-size:16px;font-weight:500}
.field{border:1px solid var(--line);border-radius:3px;height:48px;padding:0 17px;display:flex;align-items:center;font-size:11px;color:var(--muted)}
.consent{left:310px;top:1385px;width:580px}
.check{position:absolute;left:0;top:4px;width:15px;height:15px;border:1px solid var(--line);border-radius:2px}
.consent p{margin-left:28px;font-size:11.3px;line-height:20px;color:#55607a}
.submit{left:502px;top:1472px;width:195px;height:53px;border-radius:27px;background:var(--blue);color:var(--white);font-size:18px;font-weight:600;display:flex;align-items:center;justify-content:center;letter-spacing:.5px}
.mail-box{left:161px;top:1662px;width:877px;height:222px;background:var(--blue);border-radius:100px 130px 130px 0}
.mail-title{left:204px;top:1745px;color:var(--white);font-size:29px;font-weight:600;line-height:36px}
.pill{height:39px;border-radius:20px;background:var(--white);padding:0 17px;display:flex;align-items:center;font-size:13px;font-weight:600;color:var(--ink)}
.signup-btn{left:873px;top:1762px;width:132px;height:39px;border-radius:20px;background:var(--navy);color:var(--white);font-size:13px;font-weight:600;display:flex;align-items:center;justify-content:center}
.footer-nav{left:0;width:1200px;top:1958px;text-align:center;color:var(--white);font-size:15px;font-weight:500;word-spacing:2px}
.footer-nav i{font-style:normal;margin:0 22px}
.footer-rule{left:161px;top:2017px;width:879px;border-top:1px solid #33426a}
.contact-row{top:2057px;color:var(--white);font-size:14px;font-weight:600;display:flex;align-items:center;gap:10px}
.social-dot{width:28px;height:28px;border-radius:50%;background:var(--blue)}
.v-rule{top:2054px;height:30px;border-left:1px solid var(--white)}
.foot-brand{left:799px;top:2052px;display:flex;align-items:center;gap:10px;font-size:26px;font-weight:600;color:var(--blue)}
.bottom-bar{left:0;top:2125px;width:1200px;height:53px;background:var(--blue);color:var(--white);font-size:14px;font-weight:500}
</style>
</head>
<body>

<svg class="abs bg-shapes" width="1200" height="2178" aria-hidden="true">
  <path d="M0 397H1200V590C1190 720 1100 835 973 842V846H0Z" fill="var(--blue)"/>
  <rect x="1020" y="428" width="96" height="96" fill="#2bbcf2"/>
  <rect x="186" y="1224" width="56" height="100" fill="#aee3f8"/>
  <path d="M1126 730A36 36 0 0 0 1126 803Z" fill="var(--orange)"/>
  <path d="M0 2125V2040C0 1910 70 1815 161 1778V1753H1200V2125Z" fill="var(--navy)"/>
</svg>

<header class="abs site-header">
  <div class="abs brand"><span class="brand-mark"></span>Northwave Consulting</div>
  <span class="abs main-nav" style="left:505px">Home</span>
  <span class="abs main-nav" style="left:581px">About Us</span>
  <span class="abs main-nav" style="left:679px">Portfolio</span>
  <span class="abs main-nav" style="left:771px">Contact Us</span>
  <span class="abs main-nav" style="left:884px">Our Services</span>
  <span class="abs main-nav" style="left:1008px">Blog</span>
</header>

<div class="abs hero" role="img" aria-label="Photo of a hand on a laptop with floating digital marketing icons"></div>
<h1 class="abs hero-title">START YOUR PROJECT</h1>
<div class="abs crumbs"><span>Home / </span>Start Your Project</div>

<h2 class="abs section-title">START YOUR PROJECT</h2>
<p class="abs section-sub">Your Online Marketing Journey Starts Here</p>

<div class="abs form-card"></div>

<div class="abs q-row" style="top:660px">Do You Need A New Website?
  <div class="choices"><span class="choice"><span class="radio on"></span>Yes</span><span class="choice"><span class="radio"></span>No</span></div></div>
<div class="abs dash" style="top:701px"></div>
<div class="abs q-row" style="top:721px">Do You Require A New Logo or New Branding
  <div class="choices"><span class="choice"><span class="radio on"></span>Yes</span><span class="choice"><span class="radio"></span>No</span></div></div>
<div class="abs dash" style="top:761px"></div>
<div class="abs q-row" style="top:781px">Are You Interested In Online Marketing?
  <div class="choices"><span class="choice"><span class="radio on"></span>Yes</span><span class="choice"><span class="radio"></span>No</span></div></div>
<div class="abs dash" style="top:820px"></div>

<label class="abs field-label" style="top:849px">What Is Your Primary Industry?</label>
<div class="abs field" style="left:308px;top:878px;width:578px">Enter text here......</div>
<label class="abs field-label" style="top:959px">What Is The Name of Your Business</label>
<div class="abs field" style="left:308px;top:988px;width:584px">Enter text here......</div>
<label class="abs field-label" style="top:1067px">What Is Your Business Post Code</label>
<div class="abs field" style="left:308px;top:1095px;width:584px">Enter text here......</div>
<label class="abs field-label" style="top:1174px">Tell Us About Your Business?</label>
<div class="abs field" style="left:308px;top:1202px;width:584px">Enter text here......</div>
<label class="abs field-label" style="top:1284px">How Can We Get In Touch?</label>
<div class="abs field" style="left:308px;top:1312px;width:190px">Name</div>
<div class="abs field" style="left:505px;top:1312px;width:190px">example@abc.com</div>
<div class="abs field" style="left:702px;top:1312px;width:190px">xxx - xxx - xxxx</div>

<div class="abs consent"><span class="check"></span>
  <p>Your privacy is important. By using this form you consent to your form data being stored on the website's servers so that our team can access, process and contact you about your project. Please visit our privacy policy and terms and conditions for more information.</p></div>

<div class="abs submit">SUBMIT</div>

<div class="abs mail-box"></div>
<svg class="abs" style="left:169px;top:1673px" width="72" height="36" aria-hidden="true"><path d="M0 0H72A36 36 0 0 1 0 0Z" fill="var(--orange)"/></svg>
<h3 class="abs mail-title">SIGN UP TO OUR<br>MAILING LIST</h3>
<div class="abs pill" style="left:474px;top:1761px;width:184px">Name</div>
<div class="abs pill" style="left:673px;top:1761px;width:184px">Email</div>
<div class="abs signup-btn">SIGN UP NOW</div>
<svg class="abs" style="left:585px;top:1867px" width="30" height="30" aria-hidden="true"><circle cx="15" cy="15" r="15" fill="var(--mint)"/></svg>

<nav class="abs footer-nav">Home<i>|</i>About<i>|</i>Portfolio<i>|</i>Contact Us<i>|</i>Our Services<i>|</i>Blog</nav>
<div class="abs footer-rule"></div>

<div class="abs contact-row" style="left:161px">
  <svg width="15" height="11" aria-hidden="true"><rect x=".5" y=".5" width="14" height="10" fill="none" stroke="#fff"/><path d="M.5 .5L7.5 6L14.5 .5" fill="none" stroke="#fff"/></svg>
  EMAIL : <span style="font-family:Poppins,sans-serif;font-weight:400;font-size:13px">hello@northwave-example.com</span></div>
<div class="abs v-rule" style="left:454px"></div>
<div class="abs contact-row" style="left:474px;font-weight:500;font-size:15px"><span class="social-dot"></span>Socialhub</div>
<div class="abs contact-row" style="left:614px;font-weight:500;font-size:15px"><span class="social-dot"></span>Photoreel</div>
<div class="abs v-rule" style="left:746px"></div>
<div class="abs foot-brand"><span class="brand-mark"></span>Northwave</div>

<footer class="abs bottom-bar">
  <span class="abs" style="left:161px;top:17px">© 2022 Northwave Consulting . All Rights Reserved.</span>
  <span class="abs" style="left:755px;top:15px;font-weight:600">Terms and Conditions | &nbsp;Privacy policy</span>
</footer>

</body>
</html>
```